Generator Control - Superyacht Power Management System

We need a graphic design for a Touch Screen interface to control generators on Superyachts. We have a layout of the control system worked out, but need nice graphics to go with it.
The graphics comes down to a 300x460px App that i replicate several times on my 15" touchscreen as required.
See attached images.
The interface is divided up into 4 sections:
• Section#1 - 4 rectangles for the control
• Section#2 - a vertical bar graph,
• Section#3 - a section to display custom information
• Section#4 - a circuit breaker symbol.
The dimensions in pixels must be as per the attached image.
SECTION#1:
The 4 control rectangles correspond to 4 control modes:
• STOP – colours based on RED
• RUN – colours based on ORANGE
• RUN ONLINE – colours based on GREEN
• AUTO – colours based on BLUE
• THE TEXT DOESN’T HAVE TO BE ON THE GRAPHICS, WE JUST NEED THE BACKGROUND FOR THE TEXT, I ADD THE TEXT LATER USING SOFTWARE.
Each control rectangle needs to have 3 clearly identifiable states:
• Active/Selected (this is the currently active mode)
• Not Active/Not Selected (this mode is available but not currently active)
• Unavailable (this mode is not available)
SECTION#2:
The vertical bar graph design only needs the outline/frame of the bar graph. The actual moving part can be left blank; I will add that in later using an animation.
SECTION#3:
Free to look good as you want. See attached image for reference.
Within section#3 (at the top) is a 40x240px subsection, and should simply by 2 states, green or 'background colour of section#3 '. (green for when the generator is running, blend with the rest of section#3 when it is not). There are about 10 different texts I add on top of that square using software, corresponding to the status of the generator (starting, deloading, synchronizing, etc.)
SECTION#4:
Graphical representation of an electrical switch. Can be in two positions: opened or closed. See attached image as reference.

Cheif Engineers /Captains on Superyachts

Graphic Design

• Must have the same graphics style as the uploaded file#2

```html
<!DOCTYPE html>
<html lang="en">
<head>
<meta charset="utf-8">
<title>Generator Control Panel</title>
<link href="https://fonts.googleapis.com/css2?family=Roboto:wght@400;500&display=swap" rel="stylesheet">
<style>
  :root{
    --bg:#1b1e24;
    --panel:#20242c;
    --panel-edge:#3a4050;
    --inner-edge:#4a5166;
    --readout:#14171c;
    --readout-edge:#7a8299;
    --text:#e8e9ee;
    --label:#d9dbe2;
    --status:#30354d;
    --green-top:#3f8a1e;
    --green-bot:#1f4a0c;
    --green-text:#8fd24a;
    --orange-top:#ff9a1e;
    --orange-bot:#f0650a;
    --orange-text:#6b2a00;
    --red-top:#4a0d0d;
    --red-bot:#8a1010;
    --red-text:#e0322c;
    --blue-top:#1bb6ff;
    --blue-bot:#0a88e8;
    --blue-text:#0c2a4a;
    --switch:#e0201c;
  }
  *{box-sizing:border-box;margin:0;padding:0}
  html,body{width:783px;height:1200px;overflow:hidden;background:var(--bg)}
  body{font-family:"Roboto",Arial,sans-serif;color:var(--text)}
  .app{position:absolute;left:0;top:0;width:300px;height:460px;transform:scale(2.61);transform-origin:0 0;background:var(--bg)}
  .breaker{position:absolute;left:128px;top:14px;width:24px;height:46px;background:#0e0f12;border:1px solid #5a606e;border-radius:2px;padding:2px}
  .breaker .rocker{width:100%;height:100%;border-radius:2px;background:linear-gradient(180deg,#ff4a40 0%,var(--switch) 45%,#9a0e0c 100%);position:relative;box-shadow:inset 0 -3px 4px rgba(0,0,0,.35)}
  .breaker .mark{position:absolute;left:0;right:0;text-align:center;font-size:7px;color:#ffd9d6}
  .breaker .off{top:6px}
  .breaker .on{bottom:6px}
  .breaker-lead{position:absolute;left:150px;top:60px;width:1px;height:40px;background:#5a606e}
  .control-panel{position:absolute;left:5px;top:101px;width:231px;height:355px;border:1px solid var(--panel-edge);border-radius:6px;background:var(--panel)}
  .mode{position:absolute;width:106px;height:68px;border-radius:6px;display:flex;align-items:center;justify-content:center;text-align:center;font-size:12px;line-height:1.25}
  .mode.online{left:7px;top:9px;background:linear-gradient(180deg,var(--green-top),var(--green-bot));color:var(--green-text);border:1px solid #2d4a1a}
  .mode.run{left:117px;top:9px;background:radial-gradient(ellipse at 50% 45%,#ffb52a,var(--orange-bot) 90%);color:var(--orange-text);border:2px solid #fff}
  .mode.stop{left:7px;top:82px;background:linear-gradient(180deg,var(--red-top),var(--red-bot));color:var(--red-text);border:1px solid #3a1212}
  .mode.auto{left:117px;top:82px;background:radial-gradient(ellipse at 50% 45%,var(--blue-top),var(--blue-bot) 90%);color:var(--blue-text);border:2px solid #fff}
  .info-panel{position:absolute;left:5px;top:179px;width:221px;height:173px;border:1px solid var(--panel-edge);border-radius:5px}
  .status{position:absolute;left:10px;top:159px;width:210px;height:38px;background:var(--status);border-radius:6px;display:flex;align-items:center;justify-content:center;font-size:17px;letter-spacing:.2px;z-index:1}
  .readout{position:absolute;left:11px;width:67px;height:24px;background:var(--readout);border:1.5px solid var(--readout-edge);border-radius:4px;font-size:11px;display:flex;align-items:center;justify-content:center}
  .label{position:absolute;left:84px;font-size:9px;line-height:1.15;color:var(--label)}
  .electrical{position:absolute;left:155px;top:208px;width:64px;height:134px;background:var(--readout);border:1.5px solid var(--readout-edge);border-radius:4px;font-size:10px;line-height:1.2;text-align:center;padding-top:8px}
  .electrical p{margin:0}
  .electrical .gap{height:12px}
  .load-panel{position:absolute;left:246px;top:104px;width:50px;height:352px;border:1px solid var(--panel-edge);border-radius:6px;background:var(--panel)}
  .load-panel .pct{position:absolute;top:15px;left:0;right:0;text-align:center;font-size:11px;font-weight:500}
  .load-panel .pct small{font-size:7px}
  .load-panel .kw{position:absolute;top:318px;left:0;right:0;text-align:center;font-size:11px;font-weight:500;line-height:1.1}
  .load-panel .kw small{display:block;font-size:7px}
  .load-panel svg{position:absolute;left:0;top:30px}
</style>
</head>
<body>
<div class="app">
  <div class="breaker"><div class="rocker"><span class="mark off">o</span><span class="mark on">I</span></div></div>
  <div class="breaker-lead"></div>

  <section class="control-panel">
    <div class="mode online">RUN<br>ONLINE</div>
    <div class="mode run">RUN</div>
    <div class="mode stop">STOP</div>
    <div class="mode auto">AUTOMATIC</div>

    <div class="info-panel"></div>
    <div class="status">RUNNING OFFLINE</div>

    <div class="readout" style="top:207px">83 °C</div>
    <div class="label" style="top:211px">WATER<br>TEMP</div>
    <div class="readout" style="top:245px">3.8 BAR</div>
    <div class="label" style="top:247px">OIL<br>PRESSURE</div>
    <div class="readout" style="top:281px">1500</div>
    <div class="label" style="top:289px">RPM</div>
    <div class="readout" style="top:316px">0h 0m 0s</div>
    <div class="label" style="top:318px">ONLINE<br>TIME</div>

    <div class="electrical">
      <p>230 VAC</p><p>400 VAC</p><p>50.0 Hz</p>
      <div class="gap"></div>
      <p>0 A L1</p><p>0 A L2</p><p>0 A L3</p>
      <div class="gap"></div>
      <p>0 KVA</p><p>0.00 PF</p>
    </div>
  </section>

  <aside class="load-panel">
    <div class="pct">0 <small>%</small></div>
    <svg width="50" height="285" viewBox="0 0 50 285" aria-label="Load bar graph">
      <defs>
        <linearGradient id="rib" x1="0" x2="1">
          <stop offset="0" stop-color="#6a6f78"/><stop offset=".5" stop-color="#c9ccd2"/><stop offset="1" stop-color="#5a5f68"/>
        </linearGradient>
      </defs>
      <rect x="17" y="4" width="26" height="276" rx="7" fill="#0e1014" stroke="#3e4452"/>
      <g fill="url(#rib)">
        <rect x="20" y="8" width="20" height="8" rx="3"/><rect x="20" y="18" width="20" height="8" rx="3"/>
        <rect x="20" y="28" width="20" height="8" rx="3"/><rect x="20" y="38" width="20" height="8" rx="3"/>
        <rect x="20" y="48" width="20" height="8" rx="3"/><rect x="20" y="58" width="20" height="8" rx="3"/>
        <rect x="20" y="68" width="20" height="8" rx="3"/><rect x="20" y="78" width="20" height="8" rx="3"/>
        <rect x="20" y="88" width="20" height="8" rx="3"/><rect x="20" y="98" width="20" height="8" rx="3"/>
        <rect x="20" y="108" width="20" height="8" rx="3"/><rect x="20" y="118" width="20" height="8" rx="3"/>
        <rect x="20" y="128" width="20" height="8" rx="3"/><rect x="20" y="138" width="20" height="8" rx="3"/>
        <rect x="20" y="148" width="20" height="8" rx="3"/><rect x="20" y="158" width="20" height="8" rx="3"/>
        <rect x="20" y="168" width="20" height="8" rx="3"/><rect x="20" y="178" width="20" height="8" rx="3"/>
        <rect x="20" y="188" width="20" height="8" rx="3"/><rect x="20" y="198" width="20" height="8" rx="3"/>
        <rect x="20" y="208" width="20" height="8" rx="3"/><rect x="20" y="218" width="20" height="8" rx="3"/>
        <rect x="20" y="228" width="20" height="8" rx="3"/><rect x="20" y="238" width="20" height="8" rx="3"/>
        <rect x="20" y="248" width="20" height="8" rx="3"/><rect x="20" y="258" width="20" height="8" rx="3"/>
      </g>
      <rect x="20" y="268" width="20" height="8" rx="3" fill="#c0221c"/>
      <g fill="#9aa0ac" font-size="6" font-family="Roboto, Arial, sans-serif" text-anchor="middle">
        <text transform="translate(11 12) rotate(90)">100</text>
        <text transform="translate(11 140) rotate(90)">50</text>
        <text transform="translate(11 271) rotate(90)">0</text>
      </g>
      <g stroke="#6a707c" stroke-width=".6">
        <line x1="13" y1="8" x2="13" y2="276"/>
      </g>
    </svg>
    <div class="kw">0<small>KW</small></div>
  </aside>
</div>
</body>
</html>
```